Velvetorchid Hair & Beauty Business Card

Velvetorchid Hair & Beauty is a boutique salon located in the picturesque Lake Taupo NZ. The salon is very luxurious, opulent gold gilded mirrors, chandelier lit, contemporary french decor, sets the mood to create beautiful hair, makeup and all beauty services. Just had a new logo design and now after a new business card.
Logo
14 Korowhai Street
Taupo
Phone (07) 548 6193
www.velvetorchid.co.nz
email hair@velvetorchid.co.nz
Marlena Swithin
Also need a space to put in Stylist name, date, appointment time. thanks;)
Another idea is we could incorporate the wallpaper in the back ground either on the back or front or use an ornate glided frame (around the edge of the card) like on my website where my brides photos flash.
Decided against the wall paper but at least you can see our colour theme for the salon.
Updates

Please check out my updated brief . Thanks :)

Target Market(s)

25-60 years plus, mainly mid age females , wanting the best possible service , high standard of workmanship and money not a problem.

Industry/Entity Type

Boutique

Requirements
Must have
• Gold and silver

```html
<!DOCTYPE html>
<html lang="en">
<head>
<meta charset="utf-8">
<title>Velvetorchid Hair &amp; Beauty – Business Card</title>
<link href="https://fonts.googleapis.com/css2?family=Mulish:wght@400;700&display=swap" rel="stylesheet">
<style>
  :root {
    --backdrop: #2b2929;
    --card-gold: #7a6410;
    --card-black: #0b0b0b;
    --edge-black: #080808;
    --ornament-gold: #8f7a3a;
    --ornament-dark: #685511;
    --logo-gold: #b49a4e;
    --text-light: #ffffff;
    --text-ink: #1a1606;
  }
  * { box-sizing: border-box; margin: 0; padding: 0; }
  html, body {
    width: 1200px; height: 900px; overflow: hidden;
    background: var(--backdrop);
    font-family: "Mulish", "Century Gothic", sans-serif;
  }
  .canvas { position: relative; width: 1200px; height: 900px; }

  .card {
    position: absolute; width: 660px; height: 378px;
    box-shadow: 0 10px 28px rgba(0,0,0,.45);
    overflow: hidden;
  }

  /* Front: contact side */
  .card--front {
    left: 90px; top: 60px;
    background: var(--card-gold);
    border-left: 22px solid var(--edge-black);
    border-right: 22px solid var(--edge-black);
  }
  .holder-name {
    position: absolute; left: 28px; top: 46px;
    color: var(--text-light); font-weight: 700; font-size: 29px; letter-spacing: .5px;
  }
  .ornament {
    position: absolute; border-radius: 40px;
  }
  .ornament--front-top {
    left: 60px; top: 92px; width: 290px; height: 70px;
    background: linear-gradient(180deg, var(--ornament-dark), #5e4c0e 60%, var(--ornament-dark));
  }
  .ornament--front-bottom {
    left: 360px; top: 258px; width: 230px; height: 66px;
    background: linear-gradient(180deg, var(--ornament-dark), #5e4c0e 60%, var(--ornament-dark));
  }
  .contact-list {
    position: absolute; left: 345px; top: 40px; list-style: none;
  }
  .contact-item {
    display: flex; align-items: center; gap: 8px;
    color: var(--text-light); font-size: 14px; height: 28px;
  }
  .contact-icon { width: 18px; height: 18px; flex: none; }

  .appointment {
    position: absolute; left: 26px; top: 248px; width: 210px;
  }
  .appointment-row {
    display: flex; align-items: flex-end; height: 22px;
    border-bottom: 1px solid var(--text-ink);
    color: var(--text-ink); font-size: 13px; padding-bottom: 1px;
  }

  /* Back: brand side */
  .card--back {
    left: 450px; top: 470px;
    background: var(--card-black);
  }
  .ornament--back {
    left: 190px; top: 70px; width: 280px; height: 84px;
    background: linear-gradient(180deg, #4e4220, #6d5d2c 55%, #3e3519);
  }
  .brand {
    position: absolute; left: 0; right: 0; top: 168px; text-align: center;
  }
  .brand-name {
    color: var(--logo-gold); font-weight: 400; font-size: 46px; letter-spacing: 1px;
    line-height: 1.1;
  }
  .brand-rule {
    display: block; width: 480px; height: 2px; margin: 22px auto 0;
    background: var(--logo-gold);
  }
</style>
</head>
<body>
<main class="canvas">

  <section class="card card--front" aria-label="Business card front">
    <div class="ornament ornament--front-top" role="img" aria-label="Gold baroque scroll ornament"></div>
    <div class="ornament ornament--front-bottom" role="img" aria-label="Gold baroque scroll ornament"></div>

    <h1 class="holder-name">Marlena Swithin</h1>

    <ul class="contact-list">
      <li class="contact-item">
        <svg class="contact-icon" viewBox="0 0 18 18" aria-hidden="true"><circle cx="9" cy="9" r="9" fill="#fff"/><path d="M6 4.5l2 2-1 1.3c.6 1.3 1.6 2.3 2.9 2.9l1.3-1 2 2-1.2 1.3C8.8 13 5 9.2 4.7 5.7z" fill="#3a300a"/></svg>
        (07) 548 6193
      </li>
      <li class="contact-item">
        <svg class="contact-icon" viewBox="0 0 18 18" aria-hidden="true"><circle cx="9" cy="9" r="9" fill="#fff"/><path d="M9 3.5a3.6 3.6 0 0 0-3.6 3.6C5.4 10 9 14 9 14s3.6-4 3.6-6.9A3.6 3.6 0 0 0 9 3.5z" fill="#3a300a"/><circle cx="9" cy="7.2" r="1.3" fill="#fff"/></svg>
        14 Korowhai Street, Taupo
      </li>
      <li class="contact-item">
        <svg class="contact-icon" viewBox="0 0 18 18" aria-hidden="true"><circle cx="9" cy="9" r="9" fill="#fff"/><text x="9" y="12.6" text-anchor="middle" font-size="11" font-weight="700" fill="#3a300a" font-family="Mulish, sans-serif">@</text></svg>
        hair@velvetorchid.co.nz
      </li>
      <li class="contact-item">
        <svg class="contact-icon" viewBox="0 0 18 18" aria-hidden="true"><circle cx="9" cy="9" r="9" fill="#fff"/><circle cx="9" cy="9" r="4.8" fill="none" stroke="#3a300a" stroke-width="1.2"/><ellipse cx="9" cy="9" rx="2" ry="4.8" fill="none" stroke="#3a300a" stroke-width="1"/><path d="M4.2 9h9.6" stroke="#3a300a" stroke-width="1"/></svg>
        www.velvetorchid.co.nz
      </li>
    </ul>

    <div class="appointment">
      <div class="appointment-row">Stylist</div>
      <div class="appointment-row">Date</div>
      <div class="appointment-row">Time</div>
    </div>
  </section>

  <section class="card card--back" aria-label="Business card back">
    <div class="ornament ornament--back" role="img" aria-label="Gold baroque crest ornament"></div>
    <div class="brand">
      <p class="brand-name">Velvetorchid Hair &amp; Beauty</p>
      <span class="brand-rule"></span>
    </div>
  </section>

</main>
</body>
</html>
```